そよかぜ日記(http://www.soyokaze-nikki.com/)から発刊した、Lumora電子書籍の表紙のデザインをコンペ形式で募集いたします。 電子書籍「庭仕事の始め方: 3年で畑を百坪に広げた家庭菜園術」(http://www.shoppomart.jp/exec/tenpo/item/Q77KTX3MZA/) の表紙をリニューアルします。 ファイル形式はjpeg(1600×2560px) 50MB未満でお願いします。 .psdファイルも一緒に納品してください(.pdfも可能)。 白地または非常に薄い背景色の表紙画像は、白い背景との区別がつかなくなる場合があります。幅の狭い (3 ~ 4 ピクセル) 薄灰色の枠線を追加して、表紙の境界を明確にしてください。 現在の表紙デザインに沿う必要はありません。書籍の魅力・内容をしっかりアピールしてくれるデザインを選んで採用させていただきます。 ご不明点や質問はお気軽にご相談ご相談ください。 たくさんのデザイナーの皆様からのご連絡・ご提案をお待ちしております。 |
タイトルが目につきやすいことと、シンプルですが軽くない感じのデザインが気に入りました。
皆さま、多くのご提案ありがとうございました。色々なタイプのデザインを拝見させていただくことができました。これから出版する電子書籍については、コンペで作ってもらおうと考えています。これからもよろしくお願いします。

```html
<!DOCTYPE html>
<html lang="ja">
<head>
<meta charset="utf-8">
<title>庭仕事の始め方 — 表紙</title>
<link rel="stylesheet" href="https://fonts.googleapis.com/css2?family=Yomogi&family=M+PLUS+Rounded+1c:wght@800&display=swap">
<style>
  :root {
    --board-top: #3d7a5c;
    --board-bottom: #285a42;
    --chalk-white: #f4f6f0;
    --chalk-yellow: #efe35a;
    --chalk-orange: #f2a33a;
    --tray-light: #d9dcd8;
    --tray-shadow: #9ea3a0;
    --eraser: #e6e8e6;
    --wall: #7c7468;
    --band-dark: #111111;
    --accent-blue: #1f5fd0;
    --photo-tone: #8a6a52;
    --frame: #d6d6d6;
  }
  html, body {
    margin: 0;
    padding: 0;
    width: 749px;
    height: 1200px;
    overflow: hidden;
    background: #ffffff;
  }
  .cover {
    position: relative;
    width: 749px;
    height: 1200px;
    overflow: hidden;
    box-sizing: border-box;
    border: 3px solid var(--frame);
  }
  .cover svg { display: block; }
  .title-text {
    font-family: "Yomogi", cursive;
    fill: var(--chalk-white);
    font-size: 118px;
    letter-spacing: 4px;
  }
  .author-text {
    font-family: "Yomogi", cursive;
    fill: var(--chalk-orange);
    font-size: 84px;
  }
  .tagline-text {
    font-family: "M PLUS Rounded 1c", sans-serif;
    font-weight: 800;
    font-size: 76px;
    fill: #ffffff;
    stroke: var(--accent-blue);
    stroke-width: 14px;
    stroke-linejoin: round;
    paint-order: stroke fill;
  }
</style>
</head>
<body>
<div class="cover">
  <svg width="743" height="1194" viewBox="0 0 749 1200" preserveAspectRatio="none">
    <defs>
      <linearGradient id="board" x1="0" y1="0" x2="0" y2="1">
        <stop offset="0" stop-color="var(--board-top)"/>
        <stop offset="1" stop-color="var(--board-bottom)"/>
      </linearGradient>
      <linearGradient id="wallFade" x1="0" y1="0" x2="0" y2="1">
        <stop offset="0" stop-color="var(--wall)"/>
        <stop offset="0.35" stop-color="#3a3530"/>
        <stop offset="1" stop-color="var(--band-dark)"/>
      </linearGradient>
    </defs>

    <!-- chalkboard -->
    <rect class="board" x="0" y="0" width="749" height="730" fill="url(#board)"/>

    <!-- title oval -->
    <ellipse class="title-oval" cx="395" cy="245" rx="310" ry="168" transform="rotate(-6 395 245)"
             fill="none" stroke="var(--chalk-yellow)" stroke-width="9" stroke-linecap="round" opacity="0.92"/>

    <!-- title -->
    <text class="title-text" x="150" y="225" transform="rotate(-5 380 250)">庭仕事の</text>
    <text class="title-text" x="210" y="355" transform="rotate(-5 380 250)">始め方</text>

    <!-- author -->
    <text class="author-text" x="715" y="655" text-anchor="end">そよ吉</text>

    <!-- chalk tray -->
    <rect class="tray" x="0" y="720" width="749" height="52" fill="var(--tray-light)"/>
    <rect x="0" y="764" width="749" height="10" fill="var(--tray-shadow)"/>

    <!-- lower wall and dark band -->
    <rect class="wall" x="0" y="774" width="749" height="426" fill="url(#wallFade)"/>

    <!-- erasers -->
    <rect class="eraser" x="310" y="774" width="56" height="38" rx="4" fill="var(--eraser)"/>
    <rect class="eraser" x="380" y="774" width="56" height="38" rx="4" fill="var(--eraser)"/>

    <!-- tagline -->
    <text class="tagline-text" x="38" y="880">3年で</text>
    <text class="tagline-text" x="38" y="975">畑を百坪に</text>
    <text class="tagline-text" x="38" y="1070">広げた</text>
    <text class="tagline-text" x="38" y="1165">家庭菜園術</text>

    <!-- author portrait -->
    <circle cx="622" cy="1022" r="112" fill="#ffffff"/>
    <circle cx="622" cy="1022" r="104" fill="var(--photo-tone)" role="img" aria-label="著者の顔写真"/>
  </svg>
</div>
</body>
</html>
```